I want a website to be designed for our new company, it's an import and export company for variety of things.

please see the attached Logo for our company and the Images for our different sections for our busienss

Target Market(s)

multiple

Coding

Coded - Design and coding required

Number of Pages Required

5+ page

Font styles to use
Sans Serif

Colors

Designer to choose colors to be used in the design.

Requirements
Must have
• KDR WORLDWIDE
• KDR worlwide Supply & Building provides various services. The Company offers infrastructure construction, oil, enegy and gas services, agricultural projects, real estate development, travel and tourism, and food processing and trading.
• Civil contracting for infrastructure, residential and heavy projects. Through its main subsidiaries; distribution of general food products, construction chemicals including corrosion inhibitors and electrical machinery; provides catering and travel agency services; ownership and operation of a school; offers human sources services including manpower supply.
• Drilling and Gold Mines Used Machinery, All Kinds of Construction Machinery, Drilling Machines are manufactured and sold.
Nice to have
• good designa and beautiful colours, it has too look professional

```html
<!DOCTYPE html>
<html lang="en">
<head>
<meta charset="utf-8">
<title>KDR Worldwide</title>
<link href="https://fonts.googleapis.com/css2?family=Noto+Serif&family=Montserrat:wght@400&family=Open+Sans:wght@400;700&display=swap" rel="stylesheet">
<style>
:root{
  --ink:#111;
  --dark:#262626;
  --light-text:#d8d8d8;
  --nav-text:#cfcfcf;
  --field-border:#c9c9c9;
  --muted:#666;
  --green:#3e6a2c;
  --red:#7f2222;
  --faint:#ececec;
  --black:#000;
}
*{margin:0;padding:0;box-sizing:border-box}
html,body{width:1200px;height:2664px;overflow:hidden;background:#fff}
body{position:relative;font-family:"Montserrat",sans-serif;color:var(--ink)}
.abs{position:absolute}

/* header */
.hero-bg{left:0;top:0;width:1200px;height:474px;
  background:linear-gradient(180deg,#2e2e2e 0%,#2a2a2a 30%,#1f2022 70%,#1a1b1d 100%)}
.nav{left:0;top:28px;width:1200px;display:flex;justify-content:center}
.nav a{font-size:12px;color:var(--nav-text);text-decoration:none;letter-spacing:.3px;margin:0 18px}
.brand{left:0;top:130px;width:1200px;text-align:center;font-family:"Noto Serif",serif;
  font-size:17px;letter-spacing:3px;color:var(--light-text)}

/* service tiles */
.tiles{left:100px;top:253px;display:grid;grid-template-columns:329px 329px 329px;
  grid-template-rows:161px 161px 161px;gap:7px 8px}
.tile{position:relative;display:flex;align-items:center;justify-content:center;text-align:center;
  font-family:"Noto Serif",serif;font-size:22px;line-height:29px;color:#fff;padding:0 20px}
.tile-infra{grid-column:1;grid-row:1/3;background:linear-gradient(160deg,#3b2fe0,#2a1fa6 60%,#1d1660);padding-top:16px}
.tile-oil{grid-column:2;grid-row:1;background:linear-gradient(180deg,#4a7a34,#2f5624)}
.tile-estate{grid-column:3;grid-row:1;background:linear-gradient(180deg,#9a2a2a,#7e1f1f)}
.tile-agri{grid-column:2;grid-row:2;background:linear-gradient(180deg,#8a5a20,#7d7a2a 55%,#5d6a1e);align-items:flex-start;padding-top:66px}
.tile-travel{grid-column:3;grid-row:2/4;background:linear-gradient(170deg,#3c7a34,#2f6a2c 60%,#244e22)}
.tile-food{grid-column:1/3;grid-row:3;background:linear-gradient(120deg,#8a2020,#6e1818 50%,#862626)}

/* about */
.section-title{left:0;width:1170px;text-align:center;font-family:"Noto Serif",serif;font-weight:400;font-size:46px;color:var(--ink)}
.about-title{top:822px}
.about-mark{left:646px;top:952px;width:396px;text-align:center;font-family:"Noto Serif",serif;
  font-size:28px;letter-spacing:6px;color:var(--faint)}
.about-photo{left:100px;top:965px;width:485px;height:484px;
  background:linear-gradient(160deg,#c9cfd6 0%,#8f98a3 40%,#6d7580 70%,#5a6068 100%)}
.accent-green{left:0;top:1409px;width:350px;height:70px;background:var(--green)}
.accent-red{left:585px;top:1419px;width:518px;height:20px;background:var(--red)}
.about-copy{left:655px;top:1068px;width:420px;font-size:12.4px;line-height:20px;color:#222}
.about-copy p+p{margin-top:24px}

/* contact */
.contact-bg{left:0;top:1701px;width:1200px;height:476px;
  background:linear-gradient(180deg,#ffffff 0%,#f4f5f6 25%,#e3e6e9 60%,#c9ced3 88%,#b9bfc5 100%)}
.contact-title{top:1576px}
.field{border:1px solid var(--field-border);background:rgba(255,255,255,.35);
  font-size:12px;color:var(--muted);padding-left:21px;display:flex;align-items:center}
.f-name{left:100px;top:1695px;width:492px;height:48px}
.f-email{left:607px;top:1695px;width:483px;height:48px}
.f-phone{left:100px;top:1759px;width:492px;height:47px}
.f-subject{left:607px;top:1759px;width:483px;height:47px;justify-content:space-between;padding-right:30px}
.f-message{left:100px;top:1822px;width:990px;height:163px;align-items:flex-start;padding-top:20px}
.submit{left:456px;top:2018px;width:295px;text-align:center;font-size:22px;letter-spacing:1px;color:#333;
  padding-bottom:3px;border-bottom:1px solid #666}
.footer{left:0;top:2143px;width:1200px;height:34px;background:var(--dark);display:flex;align-items:center;
  justify-content:center;font-family:"Noto Serif",serif;font-size:12px;color:#bbb}

/* designer note */
.note{font-family:"Open Sans",sans-serif;color:var(--ink)}
.note-label{left:76px;top:2223px;font-size:13px;letter-spacing:-.2px}
.note-col{font-size:18px;line-height:23.6px}
.note-col h3{font-weight:400;font-size:18px;margin-bottom:18px}
.note-left{left:76px;top:2266px;width:560px}
.note-right{left:704px;top:2267px;width:500px}
.note-bold{left:704px;top:2474px;font-size:13.5px;line-height:23px;font-weight:700}
.offer{left:0;top:2602px;width:1200px;height:62px;background:var(--black);color:#fff;
  font-family:"Open Sans",sans-serif;font-size:29px}
.offer span{position:absolute;top:12px}
</style>
</head>
<body>

<div class="abs hero-bg" role="img" aria-label="Dark mountain range silhouette at dusk"></div>
<nav class="abs nav"><a>HOME</a><a>ABOUT</a><a>SERVICES</a><a>CONTACT</a></nav>
<div class="abs brand">KDR WORLDWIDE</div>

<section class="abs tiles">
  <div class="tile tile-infra" role="img" aria-label="Construction cranes in blue light"><span>INFRASTRUCTURE<br>CONSTRUCTION</span></div>
  <div class="tile tile-oil" role="img" aria-label="Offshore oil platform at sea"><span>OIL, ENERGY AND GAS<br>SERVICES</span></div>
  <div class="tile tile-estate" role="img" aria-label="Residential building complex"><span>REAL ESTATE<br>DEVELOPMENT</span></div>
  <div class="tile tile-agri" role="img" aria-label="Tractor working crop rows in a field"><span>AGRICULTURAL PROJECTS</span></div>
  <div class="tile tile-travel" role="img" aria-label="Traveller overlooking a river between cliffs"><span>TRAVEL AND TOURISM</span></div>
  <div class="tile tile-food" role="img" aria-label="Assorted fresh fruit and vegetables"><span>FOOD PROCESSING AND TRADING</span></div>
</section>

<h2 class="abs section-title about-title">ABOUT</h2>
<div class="abs about-mark">KDR WORLDWIDE</div>
<div class="abs about-photo" role="img" aria-label="Modern office lobby with glass walls and people walking"></div>
<div class="abs accent-green"></div>
<div class="abs accent-red"></div>
<div class="abs about-copy">
  <p>Lorem ipsum dolor sit amet, consectetuer adipiscing elit, sed diam nonummy nibh euismod tincidunt ut laoreet dolore magna ali-quam erat volutpat. Ut wisi enim ad minim veniam, quis nostrud exerci tation ullamcorper suscipit lobortis nisl ut aliquip ex ea com-</p>
  <p>Lorem ipsum dolor sit amet, consectetuer adipiscing elit, sed diam nonummy nibh euismod tincidunt ut laoreet dolore magna ali-quam erat volutpat. Ut wisi enim ad minim veniam, quis nostrud exerci tation ullamcorper suscipit lobortis nisl ut aliquip ex ea com-modo consequat. Duis autem vel eum iriure dolor in hendrerit in vulputate velit esse molestie consequat, vel illum dolore eu feugiat nulla facilisis at vero eros et accumsan et iusto odio dignissim qui blandit praesent luptatum zzril delenit augue duis dolore te feu-gait nulla facilisi.</p>
</div>

<div class="abs contact-bg" role="img" aria-label="Pale misty mountain range"></div>
<h2 class="abs section-title contact-title">CONTACT US</h2>
<div class="abs field f-name">Your Name*</div>
<div class="abs field f-email">Your Email*</div>
<div class="abs field f-phone">Your Phone</div>
<div class="abs field f-subject"><span>Subject of Interest</span>
  <svg width="28" height="14" viewBox="0 0 28 14"><polyline points="1,1 14,13 27,1" fill="none" stroke="#666" stroke-width="1.2"/></svg></div>
<div class="abs field f-message">Your Message*</div>
<div class="abs submit">SUBMIT</div>
<footer class="abs footer">2020 &copy; KDR Worldwide</footer>

<div class="abs note note-label">MESSAGE FROM DESIGNER</div>
<div class="abs note note-col note-left">
  <h3>What’s included to the offer:</h3>
  -&nbsp; Fully functional website on your hosting<br>
  -&nbsp; As many pages as you will need<br>
  -&nbsp; All required installations and configurations<br>
  -&nbsp; Unlimited revisions until you happy<br>
  -&nbsp; Responsive design<br>
  -&nbsp; Any additional graphic elements ( by your request)<br>
  -&nbsp; Any additional plugins and components installation<br>
  ( like: forms, live chat, online payments,<br>
  appointment, etc)<br>
  -&nbsp; Friendly and professional support at anytime
</div>
<div class="abs note note-col note-right">
  <h3>Additional services I offer:</h3>
  -&nbsp; On-page SEO<br>
  -&nbsp; TrafficLens Analytics configuration<br>
  -&nbsp; Daily/ Weekly/ Monthly Website maintenance<br>
  -&nbsp; Website administration<br>
  -&nbsp; Regular updates<br>
  -&nbsp; Additional graphic design service...
</div>
<div class="abs note note-bold">If You’ll interested with my designs, I’ll create a LIVE DEMO page for you<br>LOOKING FORWARD TO YOUR FEEDBACKS. THANK YOU</div>

<div class="abs offer"><span style="left:273px">SPECIAL OFFER!</span><span style="left:554px">FREE Business Card design</span></div>

</body>
</html>
```